Pedalwise Touring Co Brochure

We need an informational brochure designed to display all of our cycling tours for the 2019 season. The majority of text and images can be pulled from our website - www.pedalwisetouringco.example

We would like to use the colors red (#242424), Grey, and White

```html
<!DOCTYPE html>
<html lang="en">
<head>
<meta charset="utf-8">
<title>Pedalwise Touring Co Brochure</title>
<link href="https://fonts.googleapis.com/css2?family=Montserrat:wght@400;600;700;800&family=Open+Sans:wght@400;600&display=swap" rel="stylesheet">
<style>
:root{
  --red:#b31b34;
  --dark:#242424;
  --grey:#6b6b6b;
  --light:#e9e9ea;
  --paper:#ffffff;
  --stage:#dcdcde;
}
*{box-sizing:border-box;margin:0;padding:0}
html,body{width:837px;height:1200px;overflow:hidden;background:var(--stage);font-family:"Open Sans",Arial,sans-serif;color:var(--dark)}
.spread{position:absolute;left:28px;width:782px;background:var(--paper);box-shadow:0 4px 14px rgba(0,0,0,.18);overflow:hidden}
.spread--outside{top:20px;height:520px}
.spread--inside{top:585px;height:600px}
.panel{position:absolute;top:0;height:100%}
.abs{position:absolute}
.eyebrow{font-family:"Montserrat",sans-serif;font-weight:700;color:var(--red);font-size:22px;line-height:1}
.headline{font-family:"Montserrat",sans-serif;font-weight:800;color:var(--red);font-size:17px;line-height:1.1;text-transform:uppercase;white-space:nowrap}
.photo{position:absolute}
.small{font-size:7.5px;line-height:1.45;color:var(--grey)}
.label{font-family:"Montserrat",sans-serif;font-weight:700;font-size:11px;color:var(--red)}
.brand{font-family:"Montserrat",sans-serif;font-weight:700;color:var(--red);font-size:13px;line-height:1.15}
.badge{position:absolute;width:34px;height:16px;background:#c7c9cc;border-radius:2px}
.contact-row{display:flex;align-items:center;gap:5px;margin-bottom:4px}
.contact-row svg{flex:none}
.season{font-family:"Montserrat",sans-serif;font-weight:700;color:var(--red);font-size:17px;line-height:1.2;text-transform:uppercase;text-align:center}
.url{font-family:"Montserrat",sans-serif;font-weight:600;color:var(--red);font-size:11px}
.section-title{font-family:"Montserrat",sans-serif;font-weight:700;color:var(--red);font-size:19px}
.rule{height:2px;background:var(--red);width:60px;margin:4px 0 8px}
.body{font-size:7.2px;line-height:1.55;color:var(--grey)}
.col-title{font-family:"Montserrat",sans-serif;font-weight:700;color:var(--red);font-size:10px;line-height:1.15;margin-bottom:4px}
.spec-box{position:absolute;background:var(--red);color:#fff;padding:12px 12px}
.spec-box h3{font-family:"Montserrat",sans-serif;font-weight:700;font-size:12px;margin-bottom:8px}
.spec-box li{font-size:7.5px;line-height:1.5;list-style:none;padding-left:9px;position:relative;margin-bottom:3px}
.spec-box li::before{content:"";position:absolute;left:0;top:4px;width:4px;height:4px;background:#fff;border-radius:50%}
</style>
</head>
<body>

<section class="spread spread--outside">
  <div class="panel" style="left:0;width:262px">
    <div class="abs eyebrow" style="left:22px;top:24px">IT'S</div>
    <div class="abs headline" style="left:22px;top:50px">All about the ride</div>
    <svg class="abs" style="left:0;top:92px" width="262" height="240" viewBox="0 0 262 240">
      <circle cx="128" cy="122" r="104" fill="none" stroke="var(--red)" stroke-width="10" stroke-dasharray="300 400" transform="rotate(150 128 122)"/>
    </svg>
    <div class="photo" role="img" aria-label="Mountain biker riding a forest trail" style="left:32px;top:122px;width:192px;height:192px;border-radius:50%;background:radial-gradient(circle at 45% 40%,#8a9a5b,#3f5a2c 70%,#2a3a1f)"></div>
    <div class="badge" style="left:20px;top:342px"></div>
    <div class="badge" style="left:60px;top:342px"></div>
    <div class="badge" style="left:100px;top:342px;border-radius:50%;width:16px"></div>
    <div class="badge" style="left:124px;top:342px;width:42px"></div>
    <div class="abs" style="left:20px;top:378px;width:160px">
      <div class="label" style="margin-bottom:6px">Contact Info</div>
      <div class="contact-row small"><svg width="8" height="10" viewBox="0 0 8 10"><path d="M4 0a4 4 0 0 1 4 4c0 3-4 6-4 6S0 7 0 4a4 4 0 0 1 4-4z" fill="var(--red)"/></svg>17 Alder Lane, Suite 4<br>Alder Springs, CA 95400</div>
      <div class="contact-row small"><svg width="9" height="7" viewBox="0 0 9 7"><rect width="9" height="7" fill="var(--red)"/><path d="M0 0l4.5 4L9 0" stroke="#fff" fill="none"/></svg>hello@pedalwisetouringco.example</div>
      <div class="contact-row small"><svg width="8" height="8" viewBox="0 0 8 8"><path d="M1 0h2l1 2-1 1a5 5 0 0 0 2 2l1-1 2 1v2a1 1 0 0 1-1 1A7 7 0 0 1 0 1a1 1 0 0 1 1-1z" fill="var(--red)"/></svg>+1 555 014 2280</div>
      <div class="contact-row small"><svg width="8" height="8" viewBox="0 0 8 8"><circle cx="4" cy="4" r="3.5" fill="none" stroke="var(--red)"/><path d="M.5 4h7M4 .5v7" stroke="var(--red)" stroke-width=".7"/></svg>www.pedalwisetouringco.example</div>
    </div>
    <div class="abs" style="left:168px;top:420px;display:flex;align-items:center;gap:5px">
      <span style="width:10px;height:10px;border-radius:50%;background:var(--red);flex:none"></span>
      <span class="brand" style="font-size:11px">Pedalwise<br>Touring Co</span>
    </div>
  </div>

  <div class="panel" style="left:262px;width:520px">
    <div class="photo" role="img" aria-label="Road cyclist riding along a coastal road" style="left:0;top:0;width:520px;height:400px;background:linear-gradient(180deg,#a9c6dc 0%,#cfdde6 40%,#7d8d86 70%,#5a625c 100%)"></div>
    <svg class="abs" style="left:0;top:0" width="520" height="520" viewBox="0 0 520 520">
      <path d="M0 350 Q250 430 520 300 L520 520 L0 520Z" fill="var(--paper)"/>
      <path d="M0 350 Q250 430 520 300" fill="none" stroke="var(--red)" stroke-width="5"/>
      <circle cx="425" cy="330" r="80" fill="none" stroke="var(--red)" stroke-width="14"/>
      <circle cx="425" cy="330" r="72" fill="var(--paper)"/>
    </svg>
    <div class="abs brand" style="left:375px;top:315px;width:100px;text-align:center">Pedalwise<br>Touring Co</div>
    <div class="abs season" style="left:60px;top:420px;width:270px">Cycling tours<br><span style="font-weight:800">for the 2019 season</span></div>
    <div class="abs url" style="left:75px;top:480px;width:240px;text-align:center">www.pedalwisetouringco.example</div>
  </div>
</section>

<section class="spread spread--inside">
  <div class="panel" style="left:0;width:391px">
    <div class="abs" style="left:22px;top:20px;width:240px">
      <div class="section-title">Our Story</div>
      <div class="rule"></div>
      <p class="body" style="margin-bottom:6px">Pedalwise Touring Co began with a few friends, two wheels and a love of quiet back roads. Today we guide riders of every level through the most scenic valleys, coastlines and mountain passes in North America, taking care of every detail along the way.</p>
      <p class="body" style="margin-bottom:6px">Each tour is planned by riders who know the routes by heart. We scout every climb, café and overnight stop so you can simply ride, rest and enjoy the view with a friendly, experienced crew behind you.</p>
      <p class="body">Our cycling adventures are designed for active riders who want a memorable escape on some of the finest roads and trails in North America. The focus is on the ride.</p>
    </div>
    <svg class="abs" style="left:268px;top:40px" width="110" height="110" viewBox="0 0 110 110"><circle cx="55" cy="55" r="52" fill="var(--paper)" stroke="var(--light)" stroke-width="2"/></svg>
    <div class="abs brand" style="left:273px;top:80px;width:100px;text-align:center">Pedalwise<br>Touring Co</div>
    <div class="abs" style="left:22px;top:262px;width:350px">
      <div class="section-title" style="font-size:16px;text-transform:uppercase">What sets us apart?</div>
      <div class="rule"></div>
      <div style="display:flex;gap:14px">
        <div style="flex:1"><div class="col-title">The Best Routes</div><p class="body">Hand-picked roads with low traffic, great views and well-timed rest stops on every tour day.</p></div>
        <div style="flex:1"><div class="col-title">Passion Meets Expertise</div><p class="body">Our guides are seasoned riders and mechanics who share a love of the open road.</p></div>
        <div style="flex:1"><div class="col-title">Flexibility</div><p class="body">Choose your pace, your distance and your bike. Every rider can shape the trip.</p></div>
      </div>
    </div>
    <div class="photo" role="img" aria-label="Winding country road through green hills" style="left:0;top:440px;width:391px;height:160px;background:linear-gradient(180deg,#b9cfe0 0%,#9fb57d 45%,#5f7a3e 100%)"></div>
    <svg class="abs" style="left:0;top:420px" width="391" height="180" viewBox="0 0 391 180">
      <path d="M0 20 Q200 0 391 40 L391 0 L0 0Z" fill="var(--paper)"/>
      <path d="M260 180 Q340 120 391 110 L391 180Z" fill="var(--red)"/>
    </svg>
  </div>

  <div class="panel" style="left:391px;width:391px;border-left:1px solid var(--light)">
    <svg class="abs" style="left:0;top:0" width="60" height="60" viewBox="0 0 60 60"><path d="M0 0H60L0 60Z" fill="var(--red)"/></svg>
    <div class="abs section-title" style="left:44px;top:22px;font-size:15px;text-transform:uppercase">A Premier <span style="color:var(--dark)">Cycling Experience</span></div>

    <div class="photo" role="img" aria-label="Red and white road bike" style="left:22px;top:70px;width:220px;height:130px;background:linear-gradient(135deg,#f4f4f4,#d9d9db)"></div>
    <div class="spec-box" style="left:255px;top:62px;width:124px;height:150px">
      <h3>ROAD</h3>
      <ul><li>Carbon frame and fork</li><li>Electronic 22-speed group</li><li>Hydraulic disc brakes</li><li>Fitted to your size</li></ul>
    </div>
    <p class="abs body" style="left:22px;top:222px;width:357px">Our road fleet is light, responsive and tuned before every tour. Each bike is fitted to the rider on day one, with pedals, saddle and bars adjusted for long, comfortable miles.</p>

    <div class="photo" role="img" aria-label="Black full-suspension mountain bike" style="left:22px;top:300px;width:220px;height:130px;background:linear-gradient(135deg,#f4f4f4,#d9d9db)"></div>
    <div class="spec-box" style="left:255px;top:292px;width:124px;height:150px">
      <h3>MOUNTAIN</h3>
      <ul><li>Full suspension trail frame</li><li>Wide tubeless tyres</li><li>Dropper seat post</li><li>12-speed drivetrain</li></ul>
    </div>
    <p class="abs body" style="left:22px;top:452px;width:357px">The trail bikes are built for flowing singletrack and rocky descents, with reliable suspension and brakes that give you confidence on every turn.</p>
    <p class="abs body" style="left:22px;top:500px;width:357px">Bring your own pedals or use ours. Every tour includes support vehicles, spare parts and a mechanic, so you can focus on the ride and the views around you.</p>
  </div>
</section>

</body>
</html>
```